Wix web design for healthcare IT consulting firm.

I am looking for a web design built in Wix that it will be easy for me to add or edit content in the future. The web site does not need to be overly complicated, but it should look very polished and professional. I also want to ensure it is mobile device friendly. I do not need any type of on-line purchasing ability. I will eventually do blogs, but for now it is a fairly standard web site with main page, about us, services provided, etc. I would also like a place for potential customers to contact us directly from the web site. I have included a Word document with some content for the web design. I have also included my logo and business card for reference. I would like to utilize similar colors as my business card. One of my primary competitors is https://vonmarlhq.example/

Target Market(s)

Target market could be nursing home CEO, CIO, or other leader at an organization that manages long term care facilities.

Number of Pages Required

5+ page

Colors
876aae

Requirements
Must have
• Be designed to be used in Wix. Use the content I provided to create and make web design. Allow to be viewed on mobile device. Please use similar color structure as attached business card. Please use attached logo in design.

```html
<!DOCTYPE html>
<html lang="en">
<head>
<meta charset="utf-8">
<title>Brightlane Health Systems</title>
<link rel="stylesheet" href="https://fonts.googleapis.com/css2?family=Montserrat:wght@400;500;600;700&family=Oswald:wght@400&display=swap">
<style>
:root{
  --purple:#876aae;
  --purple-dark:#6f5596;
  --ink:#222226;
  --text:#555560;
  --muted:#8a8a94;
  --line:#d9d4e4;
  --light:#f5f4f8;
  --dark:#232325;
  --white:#ffffff;
}
*{box-sizing:border-box;margin:0;padding:0}
html,body{width:1200px;height:3136px;overflow:hidden;background:var(--white)}
body{font-family:"Montserrat",sans-serif;color:var(--text);position:relative}
.abs{position:absolute}
.btn{position:absolute;display:flex;align-items:center;justify-content:center;font-size:12px;font-weight:600;border:2px solid var(--purple);color:var(--purple);background:var(--white)}
.btn--light{border-color:var(--white);color:var(--white);background:transparent}
.btn--solid{background:var(--purple);color:var(--white)}

/* header */
.site-header{position:absolute;left:0;top:0;width:1200px;height:130px;background:var(--white)}
.brand{left:42px;top:38px;display:flex;align-items:center;gap:12px;font-size:38px;font-weight:700;color:var(--purple);letter-spacing:-1px}
.brand-square{width:20px;height:20px;background:var(--purple)}
.callus{right:142px;top:26px;font-size:17px;color:var(--purple);font-weight:600;display:flex;align-items:center;gap:8px}
.callus b{color:var(--ink);font-weight:500}
.social-top{right:42px;top:28px;display:flex;gap:10px}
.social-top span{width:14px;height:14px;border:1.5px solid var(--ink)}
.main-nav{left:448px;top:78px;display:flex;font-size:12px;font-weight:600;color:var(--ink)}
.main-nav a{display:block;width:105px;text-align:center;color:inherit;text-decoration:none;white-space:nowrap}
.main-nav a.is-active{color:var(--purple)}
.nav-cta{left:999px;top:69px;width:159px;height:31px;border:none}

/* hero */
.hero{position:absolute;left:0;top:130px;width:1200px;height:520px}
.hero-photo{position:absolute;inset:0;background:linear-gradient(120deg,#9aa3ad 0%,#5f6872 35%,#3a3f46 60%,#8b939c 100%)}
.hero-shade{position:absolute;inset:0;background:linear-gradient(90deg,rgba(20,22,26,.55),rgba(20,22,26,.1))}
.hero-quote{left:200px;top:170px;font-size:31px;font-weight:700;line-height:38px;color:var(--white)}
.hero .btn{left:200px;top:311px;width:128px;height:32px}
.hero-dots{left:1006px;top:211px;display:flex;flex-direction:column;gap:11px}
.hero-dots span{width:16px;height:16px;border:2px solid var(--white);border-radius:50%}
.hero-dots span.on{background:var(--white)}

/* about */
.about{position:absolute;left:0;top:650px;width:1200px;height:320px;background:var(--purple);color:var(--white);text-align:center}
.about h2{position:absolute;top:55px;width:100%;font-size:33px;font-weight:700}
.about-lead{position:absolute;top:117px;width:100%;font-size:14px;font-weight:700}
.about-text{position:absolute;top:138px;left:280px;width:640px;font-size:13px;line-height:20px}
.about .btn{left:527px;top:223px;width:144px;height:32px}

/* services */
.services{position:absolute;left:0;top:970px;width:1200px;height:945px}
.section-title{position:absolute;width:100%;text-align:center;font-size:32px;font-weight:700;color:var(--ink)}
.services .section-title{top:58px}
.services-intro{position:absolute;top:112px;left:210px;width:780px;text-align:center;font-size:13px;line-height:21px}
.tab-line{left:200px;top:219px;width:799px;height:2px;background:var(--purple)}
.tabs{left:320px;top:200px;display:flex}
.tab{width:280px;height:39px;display:flex;align-items:center;justify-content:center;font-size:12px;font-weight:500;color:var(--purple);border:2px solid var(--purple);background:var(--white)}
.tab.is-active{background:var(--purple);color:var(--white)}
.service-grid{left:180px;top:280px;width:840px;display:grid;grid-template-columns:repeat(3,280px);grid-auto-rows:245px;row-gap:47px}
.service{position:relative;text-align:center;padding:0 22px}
.service + .service{border-left:1px solid #ececf0}
.service:nth-child(4){border-left:none}
.service::after{content:"";position:absolute;left:22px;right:22px;bottom:-24px;height:1px;background:#ececf0}
.service-num{width:46px;height:46px;margin:0 auto;border:2px solid var(--purple);color:var(--purple);font-family:"Oswald",sans-serif;font-size:24px;display:flex;align-items:center;justify-content:center}
.service-num.is-active{background:var(--purple);color:var(--white)}
.service h3{font-size:14px;font-weight:700;color:var(--ink);margin-top:14px;line-height:17px;height:34px;display:flex;align-items:flex-end;justify-content:center}
.service p{font-size:12px;line-height:17px;margin-top:14px;height:68px}
.service .more{position:static;margin:14px auto 0;width:96px;height:22px;font-size:10px}
.view-all{left:527px;top:850px;width:144px;height:32px}

/* core values */
.values{position:absolute;left:0;top:1915px;width:1200px;height:349px;background:var(--dark);color:var(--white)}
.values .section-title{top:58px;color:var(--white)}
.value{position:absolute;top:130px;width:200px;margin-left:-100px;text-align:center;font-size:13px;font-weight:600}
.value svg{display:block;margin:0 auto 14px;width:42px;height:40px;fill:var(--purple)}
.values .btn{left:537px;top:252px;width:126px;height:32px;background:transparent}

/* team */
.team{position:absolute;left:0;top:2264px;width:1200px;height:449px}
.team h2{left:200px;top:112px;font-size:32px;font-weight:700;color:var(--ink)}
.team-text{left:200px;top:170px;width:240px;font-size:12.5px;line-height:20px}
.team .btn{left:200px;top:296px;width:113px;height:32px}
.member{position:absolute;top:64px;width:238px}
.member-photo{height:241px;background:linear-gradient(180deg,#e3e3e6,#b9bcc2)}
.member-label{height:77px;display:flex;flex-direction:column;align-items:center;justify-content:center;font-size:12px;background:var(--light);color:var(--text)}
.member-label b{color:var(--purple);font-weight:600;margin-bottom:4px}
.member--lead .member-label{background:var(--purple);color:var(--white)}
.member--lead .member-label b{color:var(--white)}

/* contact */
.contact{position:absolute;left:0;top:2713px;width:1200px;height:349px;background:var(--light)}
.contact h4{position:absolute;top:58px;font-size:13px;font-weight:700;color:var(--ink)}
.contact-phone{left:200px;top:100px;font-size:26px;font-weight:700;color:var(--purple)}
.contact-phone span{color:var(--ink)}
.contact-info{left:200px;top:138px;font-size:12px;line-height:20px}
.contact-info b{display:block;color:var(--purple);font-weight:600;margin-top:14px}
.social{left:200px;top:267px;display:flex;gap:10px}
.social span{width:30px;height:30px;border:2px solid var(--muted)}
.social span.on{background:var(--purple);border-color:var(--purple)}
.field{position:absolute;height:31px;border:1px solid #c9c6d2;background:var(--white);font-size:10px;color:var(--muted);padding:9px 10px}
.field--msg{height:97px}
.contact .submit{left:481px;top:267px;width:110px;height:32px}

/* footer */
.site-footer{position:absolute;left:0;top:3062px;width:1200px;height:74px;background:var(--light)}
.footer-line{left:180px;top:0;width:840px;height:1px;background:#dcdae3}
.copy{position:absolute;top:26px;width:100%;text-align:center;font-size:11px;color:var(--ink)}
.copy span{color:var(--purple)}
</style>
</head>
<body>

<header class="site-header">
  <div class="abs brand"><span class="brand-square"></span>Brightlane</div>
  <div class="abs callus">Call Us:
    <svg width="16" height="16" viewBox="0 0 24 24" fill="none" stroke="currentColor" stroke-width="2"><path d="M5 3h4l2 5-3 2a12 12 0 0 0 6 6l2-3 5 2v4a2 2 0 0 1-2 2A18 18 0 0 1 3 5a2 2 0 0 1 2-2z"/></svg>
    <b>555-014-2290</b></div>
  <div class="abs social-top"><span></span><span></span><span></span><span></span></div>
  <nav class="abs main-nav">
    <a class="is-active" href="#">-- Home --</a><a href="#">About Us</a><a href="#">Services</a><a href="#">Team</a><a href="#">Contact Us</a>
  </nav>
  <div class="btn btn--solid nav-cta">Free Consultation</div>
</header>

<section class="hero">
  <div class="hero-photo" role="img" aria-label="Photo of two business consultants working together at a laptop in an office"></div>
  <div class="hero-shade"></div>
  <p class="abs hero-quote">"Increasing the<br>value and security of your<br>technology resources."</p>
  <div class="btn btn--light">Contact Us</div>
  <div class="abs hero-dots"><span></span><span class="on"></span><span></span><span></span></div>
</section>

<section class="about">
  <h2>About Us</h2>
  <p class="about-lead">Partner with customers to increase the value of their technology tools</p>
  <p class="about-text">There are many variations of passages of Lorem Ipsum available, but the majority have suffered alteration in some form, by injected humour, or randomised words which don't look even slightly believable. If you are going</p>
  <div class="btn btn--light">Discover More</div>
</section>

<section class="services">
  <h2 class="section-title">Our Services</h2>
  <p class="services-intro">We understand different organizations have different needs. Brightlane HS strives to assist your organization by bringing solutions that are easy to understand and allow the customer to track success. We provide solutions based on the customer's needs and desires ...</p>
  <div class="abs tab-line"></div>
  <div class="abs tabs">
    <div class="tab">Electronic Health Record (EHR)</div>
    <div class="tab is-active">Information Technology Services</div>
  </div>
  <div class="abs service-grid">
    <article class="service"><div class="service-num">01</div><h3>Risk<br>Assessment</h3><p>Provide comprehensive risk assessment including identifying all risks associated with ...</p><div class="btn more">Read More</div></article>
    <article class="service"><div class="service-num is-active">02</div><h3>Policy Management &amp;<br>Consulting</h3><p>Provide guidance on IT policy management, particularly policies required and recommended ...</p><div class="btn btn--solid more">Read More</div></article>
    <article class="service"><div class="service-num">03</div><h3>Chief Information<br>Officer</h3><p>Act as the organization's CIO or IT Director to assist with improving department's functions ...</p><div class="btn more">Read More</div></article>
    <article class="service"><div class="service-num">04</div><h3>Chief Information Security<br>Officer</h3><p>Act as the organization's CISO or Information Security Officer to assist with improving ...</p><div class="btn more">Read More</div></article>
    <article class="service"><div class="service-num">05</div><h3>IT Department<br>Evaluation</h3><p>Evaluate the department to determine potential changes or issues based on customer ...</p><div class="btn more">Read More</div></article>
    <article class="service"><div class="service-num">06</div><h3>On-Going CIO or CISO<br>Support</h3><p>Provide on-going support for an organization on a monthly fee basis ...</p><div class="btn more">Read More</div></article>
  </div>
  <div class="btn view-all">View All Services</div>
</section>

<section class="values">
  <h2 class="section-title">Core Values</h2>
  <div class="value" style="left:153px"><svg viewBox="0 0 42 40"><circle cx="12" cy="10" r="6"/><circle cx="30" cy="10" r="6"/><circle cx="21" cy="14" r="6"/><rect x="2" y="19" width="18" height="16" rx="5"/><rect x="22" y="19" width="18" height="16" rx="5"/><rect x="11" y="23" width="20" height="16" rx="5"/></svg>Customer Focused</div>
  <div class="value" style="left:391px"><svg viewBox="0 0 42 40"><path d="M2 14l10-6 9 5 9-5 10 6-6 12-13 8-13-8z"/></svg>Integrity &amp; Ethics</div>
  <div class="value" style="left:600px"><svg viewBox="0 0 42 40"><rect x="8" y="4" width="24" height="34" rx="2"/><rect x="14" y="1" width="12" height="6" rx="1" fill="#232325"/><rect x="13" y="14" width="14" height="2" fill="#232325"/><rect x="13" y="21" width="14" height="2" fill="#232325"/><rect x="13" y="28" width="10" height="2" fill="#232325"/></svg>Practice Accountability</div>
  <div class="value" style="left:823px"><svg viewBox="0 0 42 40"><rect x="6" y="24" width="7" height="14"/><rect x="17" y="16" width="7" height="22"/><rect x="28" y="8" width="7" height="30"/><path d="M4 18L18 8l6 4 12-10" stroke="#876aae" stroke-width="2" fill="none"/></svg>Professional Development</div>
  <div class="value" style="left:1047px"><svg viewBox="0 0 42 40"><path d="M8 10h9a4 4 0 1 1 8 0h9v9a4 4 0 1 1 0 8v9H8z"/></svg>Have Fun</div>
  <div class="btn">Contact Us</div>
</section>

<section class="team">
  <h2 class="abs">Our Team</h2>
  <p class="abs team-text">Contrary to popular belief, Lorem Ipsum is not simply random text. It has roots in a piece of classical Latin literature from 45 BC, making it over 2000 years old ...</p>
  <div class="btn">Read More</div>
  <div class="member member--lead" style="left:481px">
    <div class="member-photo" role="img" aria-label="Portrait photo of the president and CEO"></div>
    <div class="member-label"><b>MARCUS REED</b>President and CEO</div>
  </div>
  <div class="member" style="left:761px">
    <div class="member-photo" role="img" aria-label="Portrait photo of the vice president and CEO"></div>
    <div class="member-label"><b>DANA ELLIS</b>Vice President and CEO</div>
  </div>
</section>

<section class="contact">
  <h4 style="left:200px">Need Help? Contact Us</h4>
  <div class="abs contact-phone"><span>P.</span> 555-014-2290</div>
  <div class="abs contact-info">E.: mreed@brightlanehs.example<b>Brightlane</b>4410 Cedar Hollow Road,<br>Marlow, ST 40219</div>
  <div class="abs social"><span></span><span class="on"></span><span></span><span></span></div>
  <h4 style="left:481px">Send Us Message</h4>
  <div class="field" style="left:481px;top:109px;width:173px">Enter your Name</div>
  <div class="field" style="left:673px;top:109px;width:173px">Email</div>
  <div class="field" style="left:865px;top:109px;width:134px">Phone</div>
  <div class="field field--msg" style="left:481px;top:154px;width:518px">Message</div>
  <div class="btn submit">Submit</div>
</section>

<footer class="site-footer">
  <div class="abs footer-line"></div>
  <p class="copy">© 2018 <span>Brightlane</span>. All Right Reserved</p>
</footer>

</body>
</html>
```